We need a web design for our business in which we provide complete network packages.

Hello Designers!

First, we’d like to make clear that rather than simple web design contents. We want someone that can help design our visual branding, help us communicate a sentiment. And we are willing to pay for that.

Who are we?

We are Velcor Hub. Our company is based in Rotterdam, the Netherlands. We are providing a unique full-service concept for (wireless) communication networks within small to mid-range businesses. This means we will not only provide the hardware needed for a fast and secure network within a company, but will also install, optimize, support and maintain it. 

Velcor Hub is a new brand of a company called Trindle Works which has over 15 years of experience in the market of customer service and support. Velcor Hub is the first satellite of more to come. Like Kobi Depot and others Planets, all have a focus on full service solutions.

Velcor Hub has an experienced support center from which we can monitor our clients network in real time. Our clients don’t have to worry about anything, if something is not working correctly, we will fix it pro actively. Our clients range from education and training facilities, catering, industry, logistics, health care, consultancy agencies and high end consumers. 

In an overview all Unique Selling Points of Velcor Hub:
• Professional service, both on location and remote!
• Direct clear price indication via our unique business configuration wizard
• A specific and complete quotation after a personal intake, within two days.
• Backed by a professional call center open 12 hours a day and open on Saturdays as well.
• Backed by a professional repair center with more than 15 years of experience.
• Installation and configuration included.
• Optimization included within the first three months powered by AI and machine learning.
• Real time remote maintenance. Quality control, security and interference.

Logo
For our business we need a logo. The logo needs to tell what we stand for and what we do. It will be used in both online and offline communication to our customers. Mainly e-mail and digital forms. As Velcor Hub is one of the branches within our company we would like the logo to be part of a series in the future, which should be recognizable as part of a group of websites/brands.

Website
For our business we need a website.  The website needs a story and matching design and this is where you come in. The main focus of this website is to provide information, but more importantly to guide the user to our special quotation business configuration wizard. This business configuration wizard allows users to fill in information about their business and wish requirements, at which they will receive a real time price indication on completion. 

Configuration wizard
This business configuration wizard is developed separately by our own development team but should be part of the website in look and feel.. Our development team will develop the business configuration wizard and embed it in the website. 
The setup of the website should be focused on leading all visitors to the business configuration wizard which we create our quality leads. The website will inform the possible customers/leads on the unique selling points and then remind the customer to use the business configuration wizard to get a direct price indication. 

For the website and logo we need the whole package, the design you are creating needs to have returning elements like fonts, icons, color use,  images, maybe even characters etc. You name it! 
There needs to be a common thread in the design so we can reuse elements in, for example, the email templates, the work order or receipt we give to our customers (we may contact the winner of the contest to design these for us as well!). 

The layout needs to be complete. We want something modern. A one page design that is bright and colorful with collapsing area’s to show more information. 

Website wishes and requirements
The process:
The main function of our website, besides giving a clear indication what we do, will be to guide the user to our ‘business configuration wizard’. 

Website functionality:
Our website will be our main form of communication. We need a main/front page designed in a long single scrolling page style. Users can click on buttons to view more information. Information that was hidden before. We have included our own temporary mock ups to give you an idea of the flow we desire for the website. The titles and headers in these mock ups are in Dutch but we will translate this in the description below. These mock ups are just that, an idea about the visual presentation. You are free to implement your own design, fonts, icons, pictures etc.

The page will have 6 different areas (beside the top ‘hero’ part) and a final 7th area which is the “end page” and is a big business configuration wizard promotion.In each area you are pointed towards the business configuration wizard but if you scroll all the way down you will end up with this 7th area which is all about the wizard. However these 6 areas will need to be ‘expandable/collapsible’, meaning the user can click a “read more” button at which the element will expand to show extra information beneath it. The user can then collapse this element again by closing the part that just opened.

1. Top/Hero - Customers will be able to configure their own price indication through our wizard. So there will need to be a prominent button at the top of our main page and on the 7th area that will bring the customer to this wizard/application. This will need to be a focus throughout the whole website, meaning this button is a returning element. Furthermore the top needs two menus. One for navigating the main page itself, the other one is for switching between the different industry ‘flavors’ (Education, Logistics, Health Care etc). The idea is that the photos and text on the website will change depending on the industry picked. The design and layout remains the same however. The mock ups are based on ‘education’ and another based on logistics.

2. Real time Maintenance (Beheer) – This will be a collapsible component. It will provide a brief description of our maintenance service. The ‘configure now!’ button will need to be displayed in this area as well. This component is collapsible, meaning the user can click on a ‘Read more’ (Dutch: lees meer) button at which the element will open up to show extra information (2.1).
2.1 The extra information that can be collapsed by clicking the ‘X’ button. The headers on this page read “Carefree real time maintenance”, “Certified team of administrators”, “High service level”, “Defects immediately detected”, “Continuous remote maintenance”.

3.  Service range (Bereik) - This will be a collapsible component. It will provide a brief description of how we provide for enough wifi range within a building or company. The ‘configure now!’ button will need to be displayed in this area as well. This component is collapsible, meaning the user can click on a ‘Read more’ (Dutch: lees meer) button at which the element will open up to show extra information (3.1).
3.1 The extra information that can be collapsed by clicking the ‘X’ button. The headers on this page read “Enough range everywhere”, “Machine learning for maximum range”, “Different types of access points”, “Beamforming & Mu-MiMo”, “Multiple locations connected”.

4. Speed (Snelheid) -  This is the only component that needs to collapse twice. It will provide a brief description of how we will guarantee the fastest network speed possible. The ‘configure now!’ button will need to be displayed in this area as well. This component is collapsible, meaning the user can click on a ‘Read more’ (Dutch: lees meer) button at which the element will open up to show extra information (4.1).
4.1 The extra information that can be collapsed by clicking the ‘X’ button. The headers on this page read “Band steering, “Airtime fairness”, “Load balancing”. The user will be able to open up another element to show even more information (4.2).
4.2 This will mainly show the diagrams shown in the mock ups. It will provide extra information on what is meant by “Airtime fairness” and “Load balancing”.

5.  Manageable Costs (Beheersbare kosten) - This will be a collapsible component. It will provide a brief description of how users can manage their own costs. The ‘configure now!’ button will need to be displayed in this area as well. This component is collapsible, meaning the user can click on a ‘Read more’ (Dutch: lees meer) button at which the element will open up to show extra information (5.1).
5.1 The extra information that can be collapsed by clicking the ‘X’ button. The headers on this page read “Manageable costs”, “Upfront insight in predicated costs”, “Best price/quality ratio”, “10 years of warranty”, “High availability”.

6.  Protected and secure (Beschermd en veilig) -  This will be a collapsible component. It will provide a brief description of our protection and security guaranties. The ‘configure now!’ button will need to be displayed in this area as well. This component is collapsible, meaning the user can click on a ‘Read more’ (Dutch: lees meer) button at which the element will open up to show extra information (6.1).
6.1 The extra information that can be collapsed by clicking the ‘X’ button. The headers on this page read “Protected and Secure”, “Protected by Zenthro”, “Fire resistant and dust free”, “Managed and maintained in the Netherlands”.

7. Extras (Extra’s) - This will be a collapsible component. It will provide a brief description of additional options which our solution can provide. The ‘configure now!’ button will need to be displayed in this area as well. This component is collapsible, meaning the user can click on a ‘Read more’ (Dutch: lees meer) button at which the element will open up to show extra information (7.1).
7.1 The extra information that can be collapsed by clicking the ‘X’ button. The headers on this page read “Connection with portals like Lumigram”, “Everything in one cable”, “Cloud ready”, “Ready for even more?”.

8. unique business configuration wizard - This is the final page to (once again!) push the visitor to the ‘configure now!’ button showing some reasons to click right now.

For now, we need a logo and a website designed. We would also like a design for the configuration wizard in the same style as the website.

What we'd like:
- A modern professional, but fun, appearance
- Elements like icons to have a flat design.
- Website can be used for the different industry flavors (for example, our mockups are geared towards clients in the education sector, but we can simply swap some of the photos and content to reflect the health care sector).
- Keep in mind that the website will need to be responsive when designing!
- Create a fun and trustworthy feeling.

We will be able to provide stock photographs if necessary!

Velcor Hub

```html
<!DOCTYPE html>
<html lang="nl">
<head>
<meta charset="utf-8">
<title>Velcor Hub – Draadloze netwerken voor het onderwijs</title>
<link rel="stylesheet" href="https://fonts.googleapis.com/css2?family=Montserrat:wght@400;600;700&family=Quicksand:wght@300;400;500&family=Mulish:wght@400;600;700&display=swap">
<style>
:root{
  --navy:#0d2a6e;
  --footer:#0f2170;
  --blue:#1a6fc9;
  --cta-blue:#1565e8;
  --green:#10c510;
  --check:#17a51b;
  --ink:#555;
  --muted:#888;
  --soft:#a9a9a9;
  --red:#d9272e;
}
*{box-sizing:border-box;margin:0;padding:0}
html,body{width:800px;height:1200px;overflow:hidden;background:#fff}
body{position:relative;font-family:"Mulish",sans-serif;color:var(--ink)}
.abs{position:absolute}

/* header */
.brand{left:100px;top:14px;font-family:"Montserrat",sans-serif;font-weight:700;font-size:14px;color:var(--navy);letter-spacing:.2px}
.industry-nav{left:0;top:21px;width:800px;height:12px;font-size:6.6px;letter-spacing:.2px;color:#444;font-family:"Mulish",sans-serif;white-space:nowrap}
.industry-nav span{position:absolute;top:0}
.industry-nav span.active{border-bottom:1px solid var(--green);padding-bottom:1px}
.nav-cta{left:640px;top:19px;width:60px;height:12px;border-radius:6px;background:var(--cta-blue);color:#fff;font-size:4.6px;font-weight:700;display:flex;align-items:center;justify-content:center;letter-spacing:.2px}

/* hero */
.hero-title{left:98px;top:130px;font-family:"Montserrat",sans-serif;font-weight:600;font-size:33.5px;line-height:32px;letter-spacing:-1.4px;color:var(--navy)}
.btn{background:var(--green);color:#fff;font-family:"Montserrat",sans-serif;font-weight:700;display:flex;align-items:center;justify-content:center;text-transform:uppercase}
.hero-cta{left:100px;top:248px;width:175px;height:35px;border-radius:18px;font-size:14px;letter-spacing:-.2px}
.hero-visual{left:368px;top:94px;width:334px;height:238px;border-radius:48% 52% 42% 58% / 55% 50% 50% 45%;background:linear-gradient(135deg,#e9f8fd,#c9eef9)}
.dots{left:342px;top:367px;display:flex;gap:10px}
.dots i{display:block;width:15px;height:2px;background:#ccc}
.dots i:first-child{background:#999}

/* features */
.feature{display:flex;gap:10px;align-items:flex-start}
.feature svg{flex:none;margin-top:10px}
.feature h3{font-family:"Quicksand",sans-serif;font-weight:400;font-size:15px;line-height:12px;color:#5a5a5a;margin-bottom:4px}
.feature p{font-family:"Quicksand",sans-serif;font-size:6px;line-height:7px;color:#666;width:80px}
.feature a{display:block;margin-top:8px;font-family:"Quicksand",sans-serif;font-size:7px;color:var(--red);text-decoration:none;letter-spacing:.3px}

/* promo */
.promo-title{left:0;width:800px;top:685px;text-align:center;font-family:"Montserrat",sans-serif;font-weight:700;font-size:35px;line-height:28px;color:#666;letter-spacing:.5px}
.promo-sub{left:0;width:800px;top:757px;text-align:center;font-family:"Montserrat",sans-serif;font-size:19px;color:var(--soft)}
.promo-cta{left:330px;top:786px;width:140px;height:27px;border-radius:14px;font-size:11.5px}

.usps{left:261px;top:863px;list-style:none}
.usps li{display:flex;align-items:center;gap:10px;height:20px;margin-bottom:11px;font-family:"Mulish",sans-serif;font-size:8.6px;color:#7a7a7a;letter-spacing:.3px;text-transform:uppercase}
.usps svg{flex:none}

/* footer */
.footer{left:0;top:1025px;width:800px;height:175px;background:var(--footer);color:#fff}
.footer-col{position:absolute;top:37px;font-size:8px;line-height:18px}
.footer-col h4{font-size:8.6px;font-weight:700;letter-spacing:.3px;line-height:10px;margin-bottom:2px}
.social{position:absolute;left:341px;top:140px;display:flex;gap:4px}
.social span{display:block;width:20px;height:20px;border-radius:50%;background:#fff}
</style>
</head>
<body>

<header>
  <div class="abs brand">Velcor Hub</div>
  <nav class="abs industry-nav">
    <span class="active" style="left:321px">ONDERWIJS</span>
    <span style="left:376px">LOGISTIEK</span>
    <span style="left:424px">KANTOOR</span>
    <span style="left:471px">GEZONDHEIDSZORG</span>
    <span style="left:554px">RESTAURANT</span>
    <span style="left:613px">VILLA</span>
  </nav>
  <div class="abs nav-cta">CONFIGUREER NU</div>
</header>

<section>
  <h1 class="abs hero-title">Beheer draadloze<br>netwerken voor<br>het onderwijs</h1>
  <div class="abs btn hero-cta">Configureer nu</div>
  <div class="abs hero-visual" role="img" aria-label="Illustratie: twee zorgmedewerkers in witte jassen naast een plant en een groot hart met hartslaglijn, tegen een lichtblauwe stadsachtergrond"></div>
  <div class="abs dots"><i></i><i></i><i></i><i></i><i></i></div>
</section>

<section>
  <div class="abs feature" style="left:133px;top:455px">
    <svg width="38" height="38" viewBox="0 0 38 38" fill="none" stroke="var(--blue)" stroke-width="1.4" stroke-linecap="round"><path d="M4 33 L20 17 M20 17 a7 7 0 1 0 8-10 l-4 4 -3-1 -1-3 4-4"/><path d="M4 33 l2 2 16-16"/><circle cx="22" cy="32" r="3"/><circle cx="31" cy="29" r="3"/></svg>
    <div><h3>Beheer</h3><p>Lorem ipsum dolor sit amet, consectetur adipiscing elit, sed do eiusmod tempor</p><a>read more</a></div>
  </div>
  <div class="abs feature" style="left:332px;top:454px">
    <svg width="42" height="38" viewBox="0 0 42 38" fill="none" stroke="var(--blue)" stroke-width="1.4" stroke-linecap="round"><circle cx="26" cy="21" r="14"/><circle cx="26" cy="21" r="11"/><path d="M26 21 V14 M26 21 h4 M23 5 h6 M26 5 v2 M2 17 h7 M0 21 h9 M3 25 h6"/></svg>
    <div><h3>Snelheid</h3><p>Lorem ipsum dolor sit amet, consectetur adipiscing elit, sed do eiusmod tempor</p><a>read more</a></div>
  </div>
  <div class="abs feature" style="left:530px;top:455px">
    <svg width="44" height="38" viewBox="0 0 44 38" fill="none" stroke="var(--blue)" stroke-width="1.4"><rect x="14" y="2" width="16" height="11"/><rect x="2" y="22" width="16" height="11"/><rect x="26" y="22" width="16" height="11"/><path d="M22 13 v5 M10 18 h24 M10 18 v4 M34 18 v4 M10 33 v3 M34 33 v3"/></svg>
    <div><h3>Bereik</h3><p>Lorem ipsum dolor sit amet, consectetur adipiscing elit, sed do eiusmod tempor</p><a>read more</a></div>
  </div>

  <div class="abs feature" style="left:131px;top:564px">
    <svg width="36" height="38" viewBox="0 0 36 38" fill="none" stroke="var(--blue)" stroke-width="1.4" stroke-linecap="round"><path d="M22 8 h12 v8 h-8 M2 26 h10 l6 4 h-8 M2 26 v8 h12"/><path d="M22 12 a5 4 0 1 0 -4 6 a5 4 0 1 1 -4 6 M18 8 v22"/><path d="M6 16 h5 M28 22 h5"/></svg>
    <div><h3>Beheersbare<br>kosten</h3><p>Lorem ipsum dolor sit amet, consectetur adipiscing elit,</p><a>read more</a></div>
  </div>
  <div class="abs feature" style="left:332px;top:564px">
    <svg width="40" height="38" viewBox="0 0 40 38" fill="none" stroke="var(--blue)" stroke-width="1.4"><rect x="2" y="2" width="32" height="8" rx="4"/><rect x="2" y="11" width="32" height="8" rx="4"/><rect x="2" y="20" width="32" height="8" rx="4"/><circle cx="7" cy="6" r="1.3"/><circle cx="12" cy="6" r="1.3"/><circle cx="7" cy="15" r="1.3"/><circle cx="12" cy="15" r="1.3"/><circle cx="7" cy="24" r="1.3"/><circle cx="12" cy="24" r="1.3"/><circle cx="33" cy="33" r="4"/><path d="M29 33 h-12 v3 M22 33 v3"/></svg>
    <div><h3>Beschermd<br>en veilig</h3><p>Lorem ipsum dolor sit amet, consectetur adipiscing elit,</p><a>read more</a></div>
  </div>
  <div class="abs feature" style="left:538px;top:567px">
    <svg width="28" height="38" viewBox="0 0 28 38" fill="none" stroke="var(--blue)" stroke-width="1.4"><path d="M2 2 h18 l6 6 v28 h-24 z M20 2 v6 h6"/><circle cx="14" cy="22" r="7"/><path d="M14 18 v8 M10 22 h8 M6 8 h6 M6 11 h3"/></svg>
    <div><h3>Extra’s</h3><p>Lorem ipsum dolor sit amet, consectetur adipiscing elit, sed do eiusmod tempor</p><a>read more</a></div>
  </div>
</section>

<section>
  <h2 class="abs promo-title">intresse in de beste draadloze<br>netwerk oplossing !!</h2>
  <p class="abs promo-sub">gebruik onze unieke configurator</p>
  <div class="abs btn promo-cta">Configureer nu</div>

  <ul class="abs usps">
    <li><svg width="20" height="20" viewBox="0 0 20 20"><circle cx="10" cy="10" r="10" fill="var(--check)"/><path d="M6 10 l3 3 5-6" fill="none" stroke="#fff" stroke-width="1.8" stroke-linecap="round" stroke-linejoin="round"/></svg>Direct clear price indication</li>
    <li><svg width="20" height="20" viewBox="0 0 20 20"><circle cx="10" cy="10" r="10" fill="var(--check)"/><path d="M6 10 l3 3 5-6" fill="none" stroke="#fff" stroke-width="1.8" stroke-linecap="round" stroke-linejoin="round"/></svg>Professional service on location and remote</li>
    <li><svg width="20" height="20" viewBox="0 0 20 20"><circle cx="10" cy="10" r="10" fill="var(--check)"/><path d="M6 10 l3 3 5-6" fill="none" stroke="#fff" stroke-width="1.8" stroke-linecap="round" stroke-linejoin="round"/></svg>Optimization through AI and machine learning</li>
    <li><svg width="20" height="20" viewBox="0 0 20 20"><circle cx="10" cy="10" r="10" fill="var(--check)"/><path d="M6 10 l3 3 5-6" fill="none" stroke="#fff" stroke-width="1.8" stroke-linecap="round" stroke-linejoin="round"/></svg>Tech support 12 hours / 6 days</li>
  </ul>
</section>

<footer class="abs footer">
  <div class="footer-col" style="left:247px"><h4>CUSTOMER SERVICE</h4>Contact Us<br>FAQs</div>
  <div class="footer-col" style="left:373px"><h4>SAFETY</h4>About Us<br>Privacy Policy<br>Help</div>
  <div class="footer-col" style="left:487px"><h4>HOME</h4>My Account<br>Forgot Password<br>Account Signup</div>
  <div class="social">
    <span role="img" aria-label="Lumigram"></span>
    <span role="img" aria-label="Chirply"></span>
    <span role="img" aria-label="Linkro"></span>
    <span role="img" aria-label="Plusora"></span>
    <span role="img" aria-label="Vidnest"></span>
  </div>
</footer>

</body>
</html>
```